Chinese restaurant menu and simple logo

We need a menu design for our Chinese fast food restaurant called "Willow Spoon." We are a small take out Chinese restaurant that has limited seating. Most customers order for take-out. The restaurant has been in business for over 20 years and we need a refresh in our menu as well as logo. This restaurant has always been family run and we have many loyal customers so I would like to keep the feeling of a small business run by a family to serve your family.

For the menu:
We would like to see the colors red, yellow, and whites. I have included a menu mockup we have done but it is lacking design. I have also included pictures of the food we have taken which I would like to see some integrated into the menu. I have also included a reference/sample menu that I think should be the direction we should go in terms of design.

The menu is a trifold so it should be divided into 3 sections with each section being 8.5" x 3.6667" so the total size of the menu unfolded is the standard 8.5" x 11" letter size.

For the logo:
The original logo was just the pagoda picture from the chinese take out boxes sold everywhere with the text "Willow Spoon" above it. For the redesigned logo, we would like to keep the pagoda theme but maybe just do a silhouette of the pagoda and integrate the restaurant name "Willow Spoon" into the logo. I have included reference images of pagodas as well. I like the shape of the pagoda from file pagoda_shape.jpg. Which is a more modern silhouette of a pagoda.
Updates

Hi Designers,

I wasn't able to upload all the food photos onto the ArtMarketly website so I uploaded it to my dropbox: https://www.filecrate-share.com/sh/r4kpwx9tbnfmzle/jkP2bQC7wL

Target Market(s)

In the area of our restaurant, we serve mostly to individuals from local businesses and city hall employees for lunch and families for dinner. The demographics are mostly African American and Hispanic.

Industry/Entity Type

Fast Food Restaurant

Requirements
Must have
• The menu should be sized 8.5 inches x 11 inches unfolded. It is a tri-fold so when folded up it will be 8.5" x 3.6667".

Please use the text from files:

Pictures:
Please use pictures from my photo food library at the link here: https://www.filecrate-share.com/sh/r4kpwx9tbnfmzle/jkP2bQC7wL

```html
<!DOCTYPE html>
<html lang="en">
<head>
<meta charset="utf-8">
<title>Willow Spoon — Take-Out Menu</title>
<link rel="stylesheet" href="https://fonts.googleapis.com/css2?family=Arimo:ital,wght@0,400;1,400&family=Dancing+Script:wght@500;600&family=Uncial+Antiqua&display=swap">
<style>
  :root {
    --maroon: #520e20;
    --maroon-deep: #3e0916;
    --maroon-soft: #62142a;
    --gold: #f4c51c;
    --white: #ffffff;
    --cream: #f3ece6;
    --food-warm: #b9442b;
    --food-gold: #c98a32;
    --food-green: #6f8f3a;
  }
  * { margin: 0; padding: 0; box-sizing: border-box; }
  html, body { width: 1200px; height: 927px; overflow: hidden; background: var(--maroon); }
  .menu {
    position: relative; width: 1200px; height: 927px; overflow: hidden;
    background: radial-gradient(ellipse at 30% 40%, var(--maroon-soft), var(--maroon) 70%);
    font-family: "Arimo", Arial, sans-serif; color: var(--white);
  }
  .panel { position: absolute; top: 0; height: 927px; }
  .panel--left { left: 0; width: 397px; }
  .panel--center { left: 397px; width: 398px; background: var(--maroon-deep); }
  .panel--right { left: 795px; width: 405px; }

  .script-title {
    font-family: "Dancing Script", cursive; font-weight: 600; color: var(--gold);
    position: absolute; font-size: 44px; line-height: 1;
  }
  .offer {
    position: absolute; left: 0; width: 397px; text-align: center;
    font-style: italic; font-size: 20px; line-height: 21px; color: var(--white);
  }
  .offer .hl { color: var(--gold); }
  .price { position: absolute; font-size: 34px; color: var(--gold); font-style: normal; }

  .photo {
    position: absolute; background: var(--white); padding: 8px;
    box-shadow: 2px 3px 6px rgba(0,0,0,.4);
  }
  .photo .fill { width: 100%; height: 100%; }

  .family-list {
    position: absolute; left: 34px; top: 709px; font-style: italic;
    font-size: 19px; line-height: 18.5px;
  }
  .family-list .note { font-size: 16px; line-height: 17px; }

  .tray-strip {
    position: absolute; left: 0; top: 0; width: 398px; height: 83px;
    background: linear-gradient(90deg, var(--food-gold), var(--food-green) 25%, var(--food-warm) 50%, #c23a3a 65%, var(--food-gold) 85%);
  }
  .display {
    font-family: "Uncial Antiqua", serif; color: var(--white);
    position: absolute; left: 0; width: 398px; text-align: center; line-height: 1;
  }
  .display--main { top: 98px; font-size: 42px; }
  .display--sub { font-size: 22px; }

  .price-list { position: absolute; left: 31px; width: 336px; list-style: none; font-size: 13.5px; }
  .price-list li { display: flex; align-items: baseline; height: 18.2px; color: var(--gold); }
  .price-list .name { white-space: nowrap; }
  .price-list .dots { flex: 1; border-bottom: 1px dotted var(--gold); margin: 0 6px 3px; opacity: .8; }
  .price-list .amt { color: var(--gold); width: 36px; text-align: right; }

  .brand {
    position: absolute; left: 0; top: 330px; width: 405px; text-align: center;
    font-family: "Uncial Antiqua", serif; font-size: 46px; color: var(--white);
  }
  .tagline {
    position: absolute; left: 75px; top: 450px; width: 320px;
    font-family: "Dancing Script", cursive; font-weight: 600; font-size: 42px;
    line-height: 46px; color: var(--gold); transform: rotate(7deg); transform-origin: left top;
  }
  .address { position: absolute; left: 0; top: 614px; width: 405px; text-align: center; font-size: 18px; line-height: 23px; }
  .phone { position: absolute; left: 0; top: 704px; width: 405px; text-align: center; font-size: 36px; color: var(--gold); }
  .hours { position: absolute; left: 0; top: 760px; width: 405px; text-align: center; font-size: 17px; line-height: 22.5px; color: var(--gold); }
  .web { position: absolute; left: 0; top: 864px; width: 405px; text-align: center; font-size: 20px; text-shadow: 1px 1px 3px #000; }
</style>
</head>
<body>
<main class="menu">

  <section class="panel panel--left">
    <h2 class="script-title" style="left:108px; top:36px;">Combination</h2>
    <p class="offer" style="top:107px;">
      <span class="hl">Choose from</span> Chow Mein<span class="hl">,</span> Fried Rice<span class="hl">,</span><br>
      Steam Rice<span class="hl">,</span> Chow Fun<br>
      <span class="hl">plus</span><br>
      2 Items from Steam Table
    </p>
    <p class="price" style="left:160px; top:190px;">$ 5.79</p>

    <div class="photo" style="left:40px; top:238px; width:180px; height:180px; transform:rotate(-7deg);">
      <div class="fill" role="img" aria-label="Plate of fried rice with barbecue pork and broccoli" style="background:linear-gradient(135deg,#d9a24a,#b9442b 50%,#4f7a2e);"></div>
    </div>
    <div class="photo" style="left:200px; top:290px; width:170px; height:165px; transform:rotate(6deg);">
      <div class="fill" role="img" aria-label="Bowl of glazed chicken over rice" style="background:linear-gradient(160deg,#7a4a2a,#c07a3a 55%,#3a2a22);"></div>
    </div>

    <h2 class="script-title" style="left:102px; top:448px;">Bowl Specials</h2>
    <p class="offer" style="top:509px;">
      <span class="hl">Choose from</span> Chow Mein<span class="hl">,</span> Fried Rice<span class="hl">,</span><br>
      Steam Rice<span class="hl">,</span> Chow Fun<br>
      <span class="hl">plus</span><br>
      1 Item from Steam Table
    </p>
    <p class="price" style="left:158px; top:592px;">$ 4.39</p>

    <h2 class="script-title" style="left:34px; top:644px;">Family Meal</h2>
    <p class="family-list">
      1 Qt Pan Fried Rice<br>
      1 Qt Chow Mein<br>
      2 Qts Any Items<br>
      from Steam Table<br>
      4 Vegetable Egg Rolls<br>
      <span class="note">(Items with Shrimp<br>$1.00 extra/Qt)</span>
    </p>
    <p class="price" style="left:34px; top:837px;">$ 23.99</p>

    <div class="photo" style="left:237px; top:709px; width:142px; height:160px;">
      <div class="fill" role="img" aria-label="Take-out boxes with fried rice, noodles, orange chicken and egg rolls" style="background:linear-gradient(150deg,#e8e0d2,#c58a3a 45%,#b24a2a 70%,#6b7a3a);"></div>
    </div>
  </section>

  <section class="panel panel--center">
    <div class="tray-strip" role="img" aria-label="Party trays of chow mein, sweet and sour pork and orange chicken"></div>
    <h1 class="display display--main">party trays</h1>

    <h3 class="display display--sub" style="top:158px;">appetizers</h3>
    <ul class="price-list" style="top:192px;">
      <li><span class="name">Egg Roll (Vegetable)&nbsp; (40 pc)</span><span class="dots"></span><span class="amt">25.00</span></li>
    </ul>

    <h3 class="display display--sub" style="top:232px;">rice</h3>
    <ul class="price-list" style="top:257px;">
      <li><span class="name">Chicken Fried Rice</span><span class="dots"></span><span class="amt">22.00</span></li>
      <li><span class="name">Pork Fried Rice</span><span class="dots"></span><span class="amt">22.00</span></li>
      <li><span class="name">Shrimp Fried Rice</span><span class="dots"></span><span class="amt">35.00</span></li>
      <li><span class="name">House Special Fried Rice</span><span class="dots"></span><span class="amt">32.00</span></li>
      <li><span class="name">Vegetable Fried Rice</span><span class="dots"></span><span class="amt">20.00</span></li>
      <li><span class="name">Plain Fried Rice</span><span class="dots"></span><span class="amt">18.00</span></li>
      <li><span class="name">Steam Rice</span><span class="dots"></span><span class="amt">12.00</span></li>
    </ul>

    <h3 class="display display--sub" style="top:404px;">chow mein / chow fun</h3>
    <ul class="price-list" style="top:439px;">
      <li><span class="name">Beef Chow Mein</span><span class="dots"></span><span class="amt">24.00</span></li>
      <li><span class="name">Chicken Chow Mein</span><span class="dots"></span><span class="amt">24.00</span></li>
      <li><span class="name">Pork Chow Mein</span><span class="dots"></span><span class="amt">24.00</span></li>
      <li><span class="name">Shrimp Chow Mein</span><span class="dots"></span><span class="amt">37.00</span></li>
      <li><span class="name">Vegetable Chow Mein</span><span class="dots"></span><span class="amt">22.00</span></li>
      <li><span class="name">House Special Chow Mein</span><span class="dots"></span><span class="amt">35.00</span></li>
      <li><span class="name">Beef Chow Fun</span><span class="dots"></span><span class="amt">27.00</span></li>
      <li><span class="name">Chicken Chow Fun</span><span class="dots"></span><span class="amt">27.00</span></li>
      <li><span class="name">Pork Chow Fun</span><span class="dots"></span><span class="amt">27.00</span></li>
      <li><span class="name">Shrimp Chow Fun</span><span class="dots"></span><span class="amt">37.00</span></li>
      <li><span class="name">House Special Chow Fun</span><span class="dots"></span><span class="amt">35.00</span></li>
    </ul>

    <h3 class="display display--sub" style="top:652px;">entrees</h3>
    <ul class="price-list" style="top:676px;">
      <li><span class="name">Sweet &amp; Sour Pork</span><span class="dots"></span><span class="amt">30.00</span></li>
      <li><span class="name">Sweet &amp; Sour Chicken</span><span class="dots"></span><span class="amt">30.00</span></li>
      <li><span class="name">Stir Fried Vegetables</span><span class="dots"></span><span class="amt">25.00</span></li>
      <li><span class="name">Cha-Siu (BBQ Pork)</span><span class="dots"></span><span class="amt">37.00</span></li>
      <li><span class="name">Mushroom Chicken</span><span class="dots"></span><span class="amt">30.00</span></li>
      <li><span class="name">Orange Chicken</span><span class="dots"></span><span class="amt">32.00</span></li>
      <li><span class="name">String Bean Chicken</span><span class="dots"></span><span class="amt">32.00</span></li>
      <li><span class="name">Kung Pao Chicken *</span><span class="dots"></span><span class="amt">32.00</span></li>
      <li><span class="name">Kung Pao Shrimp *</span><span class="dots"></span><span class="amt">37.00</span></li>
      <li><span class="name">Teriyaki Chicken</span><span class="dots"></span><span class="amt">37.00</span></li>
      <li><span class="name">Broccoli Beef</span><span class="dots"></span><span class="amt">30.00</span></li>
      <li><span class="name">Broccoli Shrimp</span><span class="dots"></span><span class="amt">39.00</span></li>
    </ul>
  </section>

  <section class="panel panel--right">
    <p class="brand">Willow Spoon</p>
    <p class="tagline">The best cantonese food to take home</p>
    <p class="address">218 E. Harbor Ave.<br>(corner of Lark &amp; Harbor)<br>in the Harbor Village</p>
    <p class="phone">(555) 014-2290</p>
    <p class="hours">Open 7 Days a Week<br>Monday thru Saturday 11 AM to 9:30 PM<br>Sunday 12:00 PM to 9:30 PM</p>
    <p class="web">http://WillowSpoon.us</p>
  </section>

</main>
</body>
</html>
```